Quorvane - corporate Business Card

We need a good look and innovative business card for a new start up company based in Los Angeles called "Quorvane". We are in a payment business, including payment card, app, and ewallet. We are expert in online payment and Card not present (CNP) transaction.
We need an innovative, modern business card.

Our logo font is Aero Matics

Target Market(s)

Startup - Bank - Online Payment - Card Manufacturing

Industry/Entity Type

Startup

Contact Information for Business Card

phone: 424 555 0173 - Address: 4270 Marbrook blvd, Dunmere City, CA 90418

Requirements
Must have
• Message: innovative, professional, expert, high tech, trust, online payment expert, security
Nice to have
• no comment
Should not have
• no Comment

```html
<!DOCTYPE html>
<html lang="en">
<head>
<meta charset="utf-8">
<title>Quorvane – Business Card</title>
<link rel="stylesheet" href="https://fonts.googleapis.com/css2?family=Source+Sans+3:wght@400;600;700&display=swap">
<style>
  :root {
    --brand-red: #b71c2f;
    --blush: #f7e3e6;
    --paper: #ffffff;
    --ink: #4a4a4a;
    --stage: #e9e7e4;
  }
  * { box-sizing: border-box; margin: 0; padding: 0; }
  html, body {
    width: 1200px; height: 987px; overflow: hidden;
    background: var(--stage);
    font-family: "Source Sans 3", Arial, sans-serif;
  }
  .card {
    position: absolute; left: 293px;
    width: 615px; height: 352px;
    overflow: hidden;
    box-shadow: 0 2px 6px rgba(0,0,0,.18);
  }
  .card--front { top: 130px; background: var(--paper); }
  .card--back  { top: 506px; background: var(--brand-red); }

  .front__halo {
    position: absolute; left: 316px; top: 22px;
    width: 306px; height: 306px; border-radius: 50%;
    background: var(--blush);
  }
  .wordmark { position: absolute; display: flex; align-items: center; font-weight: 600; letter-spacing: .5px; }
  .wordmark__dot { border-radius: 50%; flex: none; }
  .front__wordmark { left: 54px; top: 57px; color: var(--brand-red); font-size: 48px; gap: 12px; }
  .front__wordmark .wordmark__dot { width: 80px; height: 80px; background: var(--brand-red); }

  .front__tab { position: absolute; left: 0; top: 225px; width: 13px; height: 43px; background: var(--brand-red); }
  .person { position: absolute; left: 54px; top: 218px; }
  .person__name { color: var(--brand-red); font-size: 23px; font-weight: 600; line-height: 1.1; }
  .person__role { color: var(--ink); font-size: 16px; margin-top: 4px; }

  .address { position: absolute; left: 388px; top: 183px; color: var(--ink); font-size: 16px; line-height: 21px; font-style: normal; }
  .contacts { position: absolute; left: 388px; top: 232px; list-style: none; color: var(--ink); font-size: 16px; }
  .contacts li { display: flex; align-items: center; gap: 9px; height: 23.5px; }
  .contacts svg { width: 15px; height: 15px; fill: var(--brand-red); flex: none; }

  .back__wordmark {
    left: 0; right: 0; top: 118px; justify-content: center;
    color: var(--paper); font-size: 68px; gap: 18px;
  }
  .back__wordmark .wordmark__dot { width: 106px; height: 106px; background: var(--paper); }
  .back__url {
    position: absolute; left: 0; right: 0; top: 288px; text-align: center;
    color: var(--paper); font-size: 15px; letter-spacing: 6px;
  }
</style>
</head>
<body>
  <section class="card card--front">
    <div class="front__halo"></div>
    <div class="wordmark front__wordmark"><span class="wordmark__dot"></span>Quorvane</div>
    <div class="front__tab"></div>
    <div class="person">
      <p class="person__name">DANA WHITLOW</p>
      <p class="person__role">CEO&amp;Founder</p>
    </div>
    <address class="address">
      4270 Marbrook blvd<br>Dunmere City, CA 90418
    </address>
    <ul class="contacts">
      <li>
        <svg viewBox="0 0 24 24" aria-hidden="true"><path d="M6.6 10.8a15.1 15.1 0 0 0 6.6 6.6l2.2-2.2a1 1 0 0 1 1-.25 11.4 11.4 0 0 0 3.6.57 1 1 0 0 1 1 1V20a1 1 0 0 1-1 1A17 17 0 0 1 3 4a1 1 0 0 1 1-1h3.5a1 1 0 0 1 1 1c0 1.25.2 2.45.57 3.57a1 1 0 0 1-.25 1z"/></svg>
        424 555 0173
      </li>
      <li>
        <svg viewBox="0 0 24 24" aria-hidden="true"><path d="M2 5h20L12 12.5z"/><path d="M2 7l10 7.5L22 7v12H2z"/></svg>
        dana@quorvane.com
      </li>
      <li>
        <svg viewBox="0 0 24 24" aria-hidden="true"><circle cx="12" cy="12" r="10"/><path d="M2 12h20M12 2c3 3 3 17 0 20M12 2c-3 3-3 17 0 20" fill="none" stroke="#fff" stroke-width="1.4"/></svg>
        www.quorvane.com
      </li>
    </ul>
  </section>

  <section class="card card--back">
    <div class="wordmark back__wordmark"><span class="wordmark__dot"></span>Quorvane</div>
    <p class="back__url">www.quorvane.com</p>
  </section>
</body>
</html>
```